Celebrity and Entertainment News Website Needed

Entertainment is one of the favors of Life and I am seeking a standard celebrity website which will discuss in depth news of different celebrities around globe with major focus on American Entertainers. There will be different categories of news from these regions. America, Europe, Asia, Australia and Africa. My website name is coralvista. Youthful colors should be used for the theme and designs, Users should be able to comment at the bottom of each news. Glossy pictures of well know celebrities should be used. Designers can get knowledge from http://qarvetto.com

```html
<!DOCTYPE html>
<html lang="en">
<head>
<meta charset="utf-8">
<title>Coralvista – Design Idea 1a</title>
<link href="https://fonts.googleapis.com/css2?family=Cabin:wght@500;600;700&family=Open+Sans:wght@400;600&family=Titillium+Web:wght@700&display=swap" rel="stylesheet">
<style>
:root{
  --backdrop:#4f3c3a;
  --title:#c7b3b0;
  --topbar:#141414;
  --header-blue:#1382d0;
  --nav-blue:#1a94df;
  --ticker-bg:#ececec;
  --ticker-text:#5a5a5a;
  --ink:#333;
  --muted:#999;
  --accent:#1a8ad6;
  --white:#fff;
}
*{box-sizing:border-box;margin:0;padding:0}
html,body{width:1200px;height:1200px;overflow:hidden}
body{background:var(--backdrop);font-family:"Open Sans",sans-serif;position:relative}
.sheet-title{position:absolute;top:36px;left:0;width:1130px;text-align:center;font-family:"Titillium Web",sans-serif;font-weight:700;font-size:36px;color:var(--title);letter-spacing:.2px;word-spacing:4px}
.site{position:absolute;left:86px;top:105px;width:1024px;height:1079px;background:var(--white);overflow:hidden}
.topbar{height:32px;background:var(--topbar);display:flex;justify-content:flex-end;align-items:center;padding-right:34px;color:#aaa;font-size:10.5px;gap:6px}
.masthead{height:96px;background:var(--header-blue);position:relative}
.brand{position:absolute;left:74px;top:30px;font-family:"Cabin",sans-serif;font-weight:700;font-size:31px;color:var(--white);letter-spacing:-.5px;text-transform:uppercase}
.ad-banner{position:absolute;left:407px;top:12px;width:582px;height:72px;background:linear-gradient(90deg,#0b3f8f,#1f6fd6 30%,#3a8ff0 55%,#1456b8 80%,#0b3a85)}
.ad-banner .ad-box{position:absolute;left:129px;top:13px;width:310px;height:45px;background:var(--white);display:flex;align-items:center;justify-content:center;font-family:"Open Sans",sans-serif;font-size:38px;color:#1d64d8;letter-spacing:-1px}
.ad-box .light{font-weight:400;color:#2f7ee8}
.nav{height:40px;background:var(--nav-blue);display:flex;align-items:center;padding:0 34px 0 45px}
.nav ul{list-style:none;display:flex;gap:21px;align-items:center}
.nav li{color:var(--white);font-weight:600;font-size:11.5px;text-transform:uppercase}
.social{margin-left:auto;display:flex;gap:10px}
.social span{width:9px;height:9px;border-radius:50%;background:var(--white);display:block}
.ticker{height:104px;background:var(--ticker-bg);border-bottom:1px solid #ddd;display:flex;padding:16px 0 0 36px}
.tick{width:159px;display:flex;gap:4px}
.tick .thumb{flex:0 0 35px;height:35px;border-radius:50%}
.tick p{font-size:10.3px;line-height:14.4px;color:var(--ticker-text);padding-right:6px}
.grid{position:absolute;left:34px;top:297px;width:955px;height:416px;display:grid;grid-template-columns:266px 1fr 267px;grid-template-rows:207px 208px;gap:1px}
.story{position:relative;overflow:hidden;display:flex;flex-direction:column;justify-content:flex-end;padding:0 16px 21px}
.story::after{content:"";position:absolute;inset:0;background:linear-gradient(180deg,rgba(0,0,0,0) 35%,rgba(0,0,0,.45))}
.story h2{position:relative;z-index:1;font-family:"Cabin",sans-serif;font-weight:600;font-size:16px;line-height:21.6px;color:var(--white)}
.story .comment{position:relative;z-index:1;font-size:10.5px;color:var(--white);margin-top:2px;display:flex;align-items:center;gap:4px}
.story.lead{grid-row:1/3;grid-column:2}
.story.lead h2{font-size:19.5px;line-height:25.6px}
.section-head{position:absolute;left:34px;top:745px;width:955px;height:25px;border-bottom:2px solid #333}
.section-head .tab{position:absolute;left:0;bottom:-2px;height:27px;width:70px;background:#333;color:var(--white);font-family:"Cabin",sans-serif;font-weight:600;font-size:12.5px;display:flex;align-items:center;justify-content:center}
.section-head .view-all{position:absolute;right:0;top:0;height:20px;width:63px;border:1px solid #ccc;font-size:8.5px;color:#555;display:flex;align-items:center;justify-content:center}
.cards{position:absolute;left:34px;top:786px;width:955px;display:grid;grid-template-columns:repeat(3,302px);column-gap:24.5px}
.card .photo{height:170px}
.card .cat{font-size:10px;color:var(--accent);margin-top:10px;text-transform:uppercase}
.card h3{font-family:"Cabin",sans-serif;font-weight:500;font-size:19px;line-height:25.6px;color:var(--ink);margin-top:2px}
.card .meta{font-size:10.5px;color:var(--muted);display:flex;align-items:center;gap:4px;margin-top:0}
</style>
</head>
<body>
<h1 class="sheet-title">Design Idea - 1a&nbsp;&nbsp; [ Top Area ]</h1>
<div class="site">
  <div class="topbar">
    <svg width="11" height="11" viewBox="0 0 11 11"><rect x="1" y="2" width="9" height="8" fill="none" stroke="#aaa"/><line x1="1" y1="4.5" x2="10" y2="4.5" stroke="#aaa"/><line x1="3.5" y1="0.5" x2="3.5" y2="3" stroke="#aaa"/><line x1="7.5" y1="0.5" x2="7.5" y2="3" stroke="#aaa"/></svg>
    <span>27th August 2016</span>
  </div>
  <header class="masthead">
    <div class="brand">Coralvista</div>
    <div class="ad-banner" role="img" aria-label="Concert crowd with raised hands behind advertising banner">
      <div class="ad-box">Advertise<span class="light">Here</span></div>
    </div>
  </header>
  <nav class="nav">
    <ul>
      <li>America</li><li>Europe</li><li>Asia</li><li>Australia</li><li>Africa</li><li>News</li>
      <li><svg width="13" height="13" viewBox="0 0 13 13"><circle cx="5.5" cy="5.5" r="4" fill="none" stroke="#fff" stroke-width="2"/><line x1="8.5" y1="8.5" x2="12" y2="12" stroke="#fff" stroke-width="2"/></svg></li>
    </ul>
    <div class="social"><span></span><span></span><span></span><span></span><span></span></div>
  </nav>
  <div class="ticker">
    <div class="tick"><div class="thumb" role="img" aria-label="Film scene thumbnail" style="background:#8a8580"></div><p>The Lindens Is Oozing With Paul Ostrander's Charm, But How Does the Rest of the Movie Hold Up?</p></div>
    <div class="tick"><div class="thumb" role="img" aria-label="Actor portrait thumbnail" style="background:#cfcac4"></div><p>Simon Fairleigh's Pictaloo Account Gets Hacked</p></div>
    <div class="tick"><div class="thumb" role="img" aria-label="Actress portrait thumbnail" style="background:#d98aa8"></div><p>Clara Benning Says They're "Thinking" About Another Lakeside Summer Sequel</p></div>
    <div class="tick"><div class="thumb" role="img" aria-label="Dancing siblings thumbnail" style="background:#9aa0ad"></div><p>Marco and Elise Danner Are Both Returning to Spotlight Steps for Season 23</p></div>
    <div class="tick"><div class="thumb" role="img" aria-label="TV cast member thumbnail" style="background:#3f6fb0"></div><p>Hollow Manor Season 2's Bloody New Photos Are Here and We Have a Lot of Questions</p></div>
    <div class="tick"><div class="thumb" role="img" aria-label="Animated series thumbnail" style="background:#b58a9c"></div><p>Lucia Prado and Victor Salas Guest Star on Brightleaf's Mira of Solvane</p></div>
  </div>

  <section class="grid">
    <article class="story" role="img" aria-label="Singer performing on stage" style="background:linear-gradient(160deg,#3a3030,#1e1a1a)">
      <h2>Marla Quist, Felix Durand &amp; More Performers Who Have Never Won a Starwave Music Award</h2>
      <div class="comment"><svg width="12" height="10" viewBox="0 0 12 10"><path d="M1 1h10v6H5L2 9V7H1z" fill="none" stroke="#fff"/></svg>Add Comment</div>
    </article>
    <article class="story lead" role="img" aria-label="Two celebrities posing in front of a car" style="background:linear-gradient(170deg,#6d6a62,#3e3c3a 55%,#222)">
      <h2>Cyrus Vell Just Surprised Mireya Santos With Literally the Biggest Gift Ever</h2>
      <div class="comment"><svg width="12" height="10" viewBox="0 0 12 10"><path d="M1 1h10v6H5L2 9V7H1z" fill="none" stroke="#fff"/></svg>Add Comment</div>
    </article>
    <article class="story" role="img" aria-label="Actress portrait with pink makeup" style="background:linear-gradient(170deg,#9a9ba3,#b7a6ad 60%,#c98fa8)">
      <h2>Greta Lindqvist's Rocking a New Shade of Pink—Makeup, That Is</h2>
      <div class="comment"><svg width="12" height="10" viewBox="0 0 12 10"><path d="M1 1h10v6H5L2 9V7H1z" fill="none" stroke="#fff"/></svg>Add Comment</div>
    </article>
    <article class="story" role="img" aria-label="Performer singing with microphone" style="background:linear-gradient(160deg,#5a5e66,#3a3a40 60%,#6a3030)">
      <h2>Otis Brenner Dishes on Nadia Kovac, Kids &amp; His Lantern Road Tour: Watch!</h2>
      <div class="comment"><svg width="12" height="10" viewBox="0 0 12 10"><path d="M1 1h10v6H5L2 9V7H1z" fill="none" stroke="#fff"/></svg>Add Comment</div>
    </article>
    <article class="story" role="img" aria-label="Songwriter standing in a dark warehouse aisle" style="background:linear-gradient(170deg,#45484c,#26282b)">
      <h2>Meet Pell Marrow, the Harmonia-Award Winning Songwriter Behind Some of Your Favorite Hits</h2>
      <div class="comment"><svg width="12" height="10" viewBox="0 0 12 10"><path d="M1 1h10v6H5L2 9V7H1z" fill="none" stroke="#fff"/></svg>Add Comment</div>
    </article>
  </section>

  <div class="section-head"><div class="tab">America</div><div class="view-all">VIEW ALL</div></div>

  <section class="cards">
    <article class="card">
      <div class="photo" role="img" aria-label="Film scene in a hospital room" style="background:linear-gradient(135deg,#8c8274,#c9c3b8 60%,#a59d92)"></div>
      <div class="cat">America</div>
      <h3>The Lindens Is Oozing With Paul Ostrander's Charm, But How Does the Rest of the Movie Hold Up?</h3>
      <div class="meta"><svg width="10" height="10" viewBox="0 0 10 10"><circle cx="5" cy="5" r="4" fill="none" stroke="#999"/><path d="M5 2.5V5h2" fill="none" stroke="#999"/></svg>10 months ago</div>
    </article>
    <article class="card">
      <div class="photo" role="img" aria-label="Smiling actor at an event backdrop" style="background:linear-gradient(135deg,#d8d4cd,#bdb7ae 55%,#e0c44a)"></div>
      <div class="cat">America</div>
      <h3>Simon Fairleigh's Pictaloo Account Gets Hacked</h3>
      <div class="meta"><svg width="10" height="10" viewBox="0 0 10 10"><circle cx="5" cy="5" r="4" fill="none" stroke="#999"/><path d="M5 2.5V5h2" fill="none" stroke="#999"/></svg>10 months ago</div>
    </article>
    <article class="card">
      <div class="photo" role="img" aria-label="Smiling actress outdoors" style="background:linear-gradient(135deg,#9a8a70,#e27fb0 55%,#c25a8c)"></div>
      <div class="cat">America</div>
      <h3>Clara Benning Says They're "Thinking" About Another Lakeside Summer Sequel</h3>
      <div class="meta"><svg width="10" height="10" viewBox="0 0 10 10"><circle cx="5" cy="5" r="4" fill="none" stroke="#999"/><path d="M5 2.5V5h2" fill="none" stroke="#999"/></svg>10 months ago</div>
    </article>
  </section>
</div>
</body>
</html>
```